Complete web design based around only our company logo

I need someone to build a web page based around our company logo. I will provide other sites that we like and would want our site to be similar to.
Updates

Please look at these websites to get an idea of our industry

larkspur minerals
tov minerals
granite royalty
windmere energy
harlow energy

Our company buys mineral rights, and royalties from mineral owners all over the united states.  We also lease minerals as well. 

What we are trying to have designed is a fully functioning website that you upload to our webhost after we approve of final design.  

Target Market(s)

Oil and Gas/Mineral Owners

Industry/Entity Type

It Company

Font styles to use
Serif
Sans Serif

Colors
9ccb3b

Requirements
Must have
• Quick Contact form

```html
<!DOCTYPE html>
<html lang="en">
<head>
<meta charset="utf-8">
<title>Copperline Holdings</title>
<link rel="stylesheet" href="https://fonts.googleapis.com/css2?family=Arimo:wght@400;700&family=Open+Sans:wght@400;600;700&display=swap">
<style>
:root{
  --green:#9ccb3b;
  --green-dark:#3f8a12;
  --ink:#333333;
  --muted:#555555;
  --rule:#dddddd;
  --panel:#ececec;
  --black:#050505;
  --white:#ffffff;
}
*{margin:0;padding:0;box-sizing:border-box}
html,body{width:1200px;height:1112px;overflow:hidden;background:var(--white)}
body{position:relative;font-family:"Arimo",Arial,sans-serif;color:var(--ink)}
.abs{position:absolute}

/* header */
.brand{left:291px;top:52px;display:flex;align-items:center;gap:8px}
.brand-mark{width:14px;height:14px;background:var(--green-dark);border-radius:50%}
.brand-name{font-weight:700;font-size:17px;line-height:19px;color:var(--green-dark);text-transform:uppercase;letter-spacing:.5px}
.nav{left:0;top:89px;width:1200px;font-size:11px;color:var(--ink)}
.nav a{position:absolute;color:inherit;text-decoration:none}
.nav a.active{color:var(--green)}
.nav-underline{left:441px;top:114px;width:47px;height:4px;background:var(--green)}
.search{left:836px;top:86px;width:108px;height:23px;border:1px solid var(--rule)}
.search svg{position:absolute;right:6px;top:5px}
.header-rule{left:289px;top:118px;width:655px;height:1px;background:var(--rule)}
.intro{left:289px;top:156px;width:655px;text-align:center;font-size:18px;line-height:21px;color:#555}
.intro em{font-style:normal;color:var(--green-dark)}

/* hero */
.band-grey{left:0;top:516px;width:1200px;height:198px;background:linear-gradient(#e4e4e4,#ffffff)}
.hero{left:290px;top:229px;width:654px;height:287px;background:#0c0c0c;overflow:hidden}
.hero-photo{position:absolute;left:150px;top:0;width:504px;height:287px;background:linear-gradient(100deg,#0d0d0d 0%,#2b2b2b 35%,#6a6a6a 70%,#3a3a3a 100%)}
.hero-title{position:absolute;left:40px;top:72px;font-size:18px;color:var(--white);letter-spacing:.3px}
.hero-sub{position:absolute;left:51px;top:98px;font-size:8.5px;color:var(--green)}
.field{position:absolute;background:var(--white);font-size:7px;color:#999;padding:0 7px;line-height:23px}
.field.email{left:42px;top:136px;width:226px;border:1px solid var(--green)}
.field.first{left:42px;top:168px;width:110px;height:25px;line-height:25px}
.field.last{left:158px;top:168px;width:110px;height:25px;line-height:25px}
.quote-btn{position:absolute;left:42px;top:205px;width:226px;height:23px;background:var(--green);color:#111;font-size:12px;line-height:23px;text-align:center}
.hero-tag{position:absolute;right:12px;top:176px;text-align:right;color:var(--white);font-family:"Open Sans",sans-serif;font-weight:600}
.hero-tag b{display:block;font-size:26px;line-height:30px;font-weight:600}
.hero-tag span{display:block;font-size:14px;line-height:16px}
.arrow-btn{top:358px;width:38px;height:38px;border-radius:50%;background:var(--white)}
.arrow-btn.prev{left:232px;border:1.5px solid #aaa}
.arrow-btn.next{left:963px;border:1.5px solid var(--green)}
.arrow-btn svg{position:absolute;left:12px;top:11px}

/* feature panel */
.features{left:290px;top:516px;width:654px;height:198px;background:var(--green);color:#222;font-size:8.5px;line-height:14px}
.features h3{position:absolute;font-size:9px;font-weight:700;color:var(--white)}
.features p{position:absolute}
.more{position:absolute;font-size:6.5px;font-weight:700;color:#222;text-decoration:underline}
.feature-photo{position:absolute;left:240px;top:22px;width:176px;height:62px;background:linear-gradient(#8a8a8a,#5a5a5a 65%,#333)}
.checklist{position:absolute;left:453px;top:47px;list-style:none}
.checklist li{display:flex;align-items:center;gap:8px;height:16.5px;font-size:8.5px}
.checklist li:first-child{color:var(--white);text-decoration:underline}

/* about */
.about-photo{left:289px;top:752px;width:247px;height:144px;background:#000;padding:6px}
.about-photo div{width:100%;height:100%;border:1px solid var(--green);padding:6px}
.about-photo div div{border:0;padding:0;background:linear-gradient(#aaa,#7a7a7a 70%,#3f3f3f)}
.about-title{left:562px;top:749px;font-size:14px;color:var(--green-dark)}
.about-text{left:562px;top:778px;width:382px;font-size:8.5px;line-height:13.3px;color:#222}
.links{left:562px;top:853px;width:382px;height:40px}
.links a{position:absolute;display:flex;align-items:center;gap:8px;font-size:8.5px;color:#222;text-decoration:underline}

/* newsletter */
.strip{left:289px;top:936px;width:655px;height:68px;border-top:3px solid var(--green);background:var(--panel)}
.strip-brand{position:absolute;left:10px;top:24px;display:flex;align-items:center;gap:4px}
.strip-brand i{width:7px;height:7px;background:var(--green-dark);border-radius:50%}
.strip-brand b{font-size:8px;line-height:9px;color:var(--green-dark);text-transform:uppercase}
.strip h4{position:absolute;left:72px;top:17px;font-size:11px;font-weight:400;color:#333}
.strip p{position:absolute;left:74px;top:38px;width:200px;font-size:7px;line-height:9.5px;color:#444}
.strip p a{color:var(--green-dark);text-decoration:none}
.signup{position:absolute;left:347px;top:0;width:308px;height:65px;background:#dcdcdc}
.signup h4{left:10px;top:21px;font-size:11px}
.signup small{position:absolute;left:11px;top:38px;font-size:5.5px;color:#666}
.signup .input{position:absolute;left:162px;top:20px;width:109px;height:25px;background:var(--white);border:1px solid var(--green);font-size:6.5px;color:#888;line-height:23px;padding-left:8px}
.signup .go{position:absolute;left:271px;top:20px;width:28px;height:25px;background:var(--green);color:var(--white);font-size:7px;font-weight:700;text-align:center;line-height:25px}

/* footer */
.footer{left:0;top:1039px;width:1200px;height:73px;background:var(--black);border-top:2px solid var(--green)}
.footer-brand{position:absolute;left:290px;top:30px;font-size:14px;line-height:16px;font-weight:700;color:var(--green);text-transform:uppercase}
.footer-nav{position:absolute;left:402px;top:34px;display:flex;gap:12px;font-size:6px;color:#888}
.footer-nav span:first-child{color:var(--green)}
.footer-legal{position:absolute;left:402px;top:50px;font-size:6px;color:#888}
.follow{position:absolute;left:905px;top:32px;font-size:6px;font-weight:700;color:var(--white)}
.social{position:absolute;top:49px;width:13px;height:13px;background:#555}
</style>
</head>
<body>

<header>
  <div class="abs brand"><span class="brand-mark"></span><span class="brand-name">Copperline<br>Holdings</span></div>
  <nav class="abs nav">
    <a class="active" style="left:445px">About Us</a>
    <a style="left:519px">Our Industry</a>
    <a style="left:597px">Lorem Ipsum</a>
    <a style="left:680px">Contact Us</a>
    <a style="left:769px">Blogs</a>
  </nav>
  <div class="abs nav-underline"></div>
  <div class="abs search"><svg width="11" height="11" viewBox="0 0 11 11"><circle cx="4.5" cy="4.5" r="3.3" fill="none" stroke="#999" stroke-width="1.2"/><line x1="7" y1="7" x2="10" y2="10" stroke="#999" stroke-width="1.4"/></svg></div>
  <div class="abs header-rule"></div>
  <p class="abs intro">Lorem ipsum dolor sit amet, <em>consectetur adipisicing elit</em>, sed do eiusmod<br>tempor incididunt ut labore et dolore magna aliqua.</p>
</header>

<div class="abs band-grey"></div>

<section class="abs hero">
  <div class="hero-photo" role="img" aria-label="Hand touching a tablet showing a rising stock chart in front of a market board"></div>
  <h1 class="hero-title" style="font-weight:400">WELCOME TO OUR WEBSITE</h1>
  <p class="hero-sub">Lorem ipsum dolor sit amet, consectetur adipisicing elit</p>
  <div class="field email">Your email</div>
  <div class="field first">Your &nbsp;Name</div>
  <div class="field last">Your Last Name</div>
  <div class="quote-btn">Get a Free Quote Now !</div>
  <div class="hero-tag"><b>A high income nation</b><span>through a flourishing oil &amp; gas economy</span></div>
</section>
<div class="abs arrow-btn prev"><svg width="12" height="14" viewBox="0 0 12 14"><polyline points="8,1 2,7 8,13" fill="none" stroke="#999" stroke-width="1.5"/></svg></div>
<div class="abs arrow-btn next"><svg width="12" height="14" viewBox="0 0 12 14"><polyline points="3,1 9,7 3,13" fill="none" stroke="#999" stroke-width="1.5"/></svg></div>

<section class="abs features">
  <h3 style="left:19px;top:20px">HEADING</h3>
  <p style="left:19px;top:47px;width:180px">Lorem ipsum dolor sit amet, consectetur adipisicing elit, sed do eiusmod tempor incididunt ut labore et dolore magna aliqua.</p>
  <p style="left:19px;top:99px;width:180px">Ut enim ad minim veniam, quis nostrud exercitation ullamco laboris nisi ut aliquip ex ea commodo consequat.</p>
  <a class="more" style="left:20px;top:163px;color:#fff">view more &gt;&gt;</a>

  <div class="feature-photo" role="img" aria-label="Offshore oil rig at sea"></div>
  <h3 style="left:240px;top:99px">HEADING</h3>
  <p style="left:240px;top:119px;width:180px">Lorem ipsum dolor sit amet, consectetur adipisicing elit, sed do eiusmod tempor incididunt ut labore et dolore</p>
  <a class="more" style="left:240px;top:163px">view more &gt;&gt;</a>

  <h3 style="left:453px;top:21px">HEADING</h3>
  <ul class="checklist">
    <li><svg width="10" height="10" viewBox="0 0 10 10"><circle cx="5" cy="5" r="5" fill="#fff"/><path d="M2.5 5h4M5 3l2 2-2 2" stroke="#9ccb3b" stroke-width="1.2" fill="none"/></svg>Lorem ipsum dolor sit amet, consectetur</li>
    <li><svg width="10" height="10" viewBox="0 0 10 10"><circle cx="5" cy="5" r="5" fill="#222"/><path d="M2.5 5h4M5 3l2 2-2 2" stroke="#fff" stroke-width="1.2" fill="none"/></svg>Lorem ipsum dolor sit amet</li>
    <li><svg width="10" height="10" viewBox="0 0 10 10"><circle cx="5" cy="5" r="5" fill="#222"/><path d="M2.5 5h4M5 3l2 2-2 2" stroke="#fff" stroke-width="1.2" fill="none"/></svg>Lorem ipsum sit amet, consectetur</li>
    <li><svg width="10" height="10" viewBox="0 0 10 10"><circle cx="5" cy="5" r="5" fill="#222"/><path d="M2.5 5h4M5 3l2 2-2 2" stroke="#fff" stroke-width="1.2" fill="none"/></svg>Lorem ipsum dolor sit amet, consectetur</li>
    <li><svg width="10" height="10" viewBox="0 0 10 10"><circle cx="5" cy="5" r="5" fill="#222"/><path d="M2.5 5h4M5 3l2 2-2 2" stroke="#fff" stroke-width="1.2" fill="none"/></svg>Lorem &nbsp;sit amet, consectetur</li>
  </ul>
  <a class="more" style="left:453px;top:163px">view more &gt;&gt;</a>
</section>

<section>
  <div class="abs about-photo"><div><div role="img" aria-label="Offshore drilling platform in grey sea"></div></div></div>
  <h2 class="abs about-title" style="font-weight:400">Lorem ipsum dolor sit amet</h2>
  <p class="abs about-text">Lorem ipsum dolor sit amet, consectetur adipisicing elit, sed do eiusmod tempor incididunt ut labore et dolore magna aliqua. Ut enim ad minim veniam, quis nostrud exercitation ullamco laboris nisi ut aliquip ex ea commodo consequat. Lorem ipsum dolor sit amet, consectetur adipisicing elit, sed do eiusmod tempor incididunt ut labore et dolore magna aliqua. Ut enim ad minim veniam, quis nostrud exercitation ullamco laboris nisi ut aliquip ex ea commodo consequat.</p>
  <div class="abs links">
    <a style="left:0;top:0"><svg width="10" height="10" viewBox="0 0 10 10"><circle cx="5" cy="5" r="5" fill="#222"/><path d="M2.5 5h4M5 3l2 2-2 2" stroke="#9ccb3b" stroke-width="1.2" fill="none"/></svg>Lorem ipsum dolor</a>
    <a style="left:136px;top:0"><svg width="10" height="10" viewBox="0 0 10 10"><circle cx="5" cy="5" r="5" fill="#222"/><path d="M2.5 5h4M5 3l2 2-2 2" stroke="#9ccb3b" stroke-width="1.2" fill="none"/></svg>Lorem ipsum dolor</a>
    <a style="left:278px;top:0"><svg width="10" height="10" viewBox="0 0 10 10"><circle cx="5" cy="5" r="5" fill="#222"/><path d="M2.5 5h4M5 3l2 2-2 2" stroke="#9ccb3b" stroke-width="1.2" fill="none"/></svg>Lorem ipsum dolor</a>
    <a style="left:0;top:18px;color:#3f8a12"><svg width="10" height="10" viewBox="0 0 10 10"><circle cx="5" cy="5" r="5" fill="#222"/><path d="M2.5 5h4M5 3l2 2-2 2" stroke="#fff" stroke-width="1.2" fill="none"/></svg>Lorem ipsum dolor</a>
    <a style="left:136px;top:18px"><svg width="10" height="10" viewBox="0 0 10 10"><circle cx="5" cy="5" r="5" fill="#222"/><path d="M2.5 5h4M5 3l2 2-2 2" stroke="#9ccb3b" stroke-width="1.2" fill="none"/></svg>Lorem ipsum dolor</a>
  </div>
</section>

<section class="abs strip">
  <div class="strip-brand"><i></i><b>Copperline<br>Holdings</b></div>
  <h4>Subheading</h4>
  <p>Lorem ipsum dolor sit amet, consectetur adipisicing elit sed do eiusmod tempor <a>more.....</a></p>
  <div class="signup">
    <h4>sign up to our newsletter</h4>
    <small>Subscribe to Copperline Holdings for news &amp; updates</small>
    <div class="input">email@example.com</div>
    <div class="go">GO</div>
  </div>
</section>

<footer class="abs footer">
  <div class="footer-brand">Copperline<br>Holdings</div>
  <div class="footer-nav"><span>About Us</span><span>Our Industry</span><span>Lorem Ipsum</span><span>Contact Us</span><span>Blogs</span></div>
  <div class="footer-legal">Privacy Policy &nbsp;| &nbsp;All Right Reserved 2014.</div>
  <div class="follow">FOLLOW US</div>
  <span class="social" style="left:874px"></span>
  <span class="social" style="left:892px"></span>
  <span class="social" style="left:910px"></span>
  <span class="social" style="left:928px"></span>
</footer>

</body>
</html>
```